We need a business card design for a Dubai based company .

We need a business card for a Dubai based company called "Zernova Smoking Requisites Trading LLC". We mainly import Flavoured Tobacco products and Charcoal which is used for smoking in a Hookah/Shisha and distribute to the wholesalers and retailers. Logo file is attached herewith.

```html
<!DOCTYPE html>
<html lang="en">
<head>
<meta charset="utf-8">
<title>Zernova Smoking Requisites Trading LLC – Business Card</title>
<link href="https://fonts.googleapis.com/css2?family=Orbitron:wght@700&family=Questrial&display=swap" rel="stylesheet">
<style>
  :root {
    --stage: #e9e7e4;
    --ink: #1b1c1e;
    --red: #c8242c;
    --white: #ffffff;
    --grey-line: #4a4b4d;
    --ghost: #2e2f31;
  }
  * { box-sizing: border-box; margin: 0; padding: 0; }
  html, body {
    width: 1200px; height: 960px; overflow: hidden;
    background: var(--stage);
  }
  .stage {
    width: 1200px; height: 960px;
    display: flex; flex-direction: column;
    align-items: center; justify-content: center; gap: 40px;
  }
  .card {
    position: relative;
    width: 760px; height: 434px;
    overflow: hidden;
    box-shadow: 0 10px 28px rgba(0,0,0,.22);
  }
  .card svg.bg { position: absolute; inset: 0; }

  /* front */
  .card--front { background: linear-gradient(120deg, #ffffff 40%, #e6e6e6 100%); }
  .holder { position: absolute; left: 40px; top: 34px; color: var(--white); font-family: "Questrial", sans-serif; }
  .holder__name { font-family: "Orbitron", sans-serif; font-weight: 700; font-size: 30px; color: var(--red); letter-spacing: .5px; }
  .holder__title { font-size: 19px; margin-top: 4px; }
  .contacts { list-style: none; margin-top: 26px; font-size: 19px; line-height: 30px; }
  .contacts li { display: flex; align-items: center; gap: 10px; }
  .contacts svg { width: 17px; height: 17px; flex: none; }
  .contacts .accent { color: var(--red); }
  .divider-dash { width: 16px; height: 2px; background: var(--red); margin: 16px 0 14px 0; }
  .address { font-size: 19px; line-height: 26px; }

  .brand { position: absolute; left: 480px; top: 176px; width: 240px; }
  .brand__name { font-family: "Questrial", sans-serif; font-size: 21px; line-height: 28px; color: var(--ink); letter-spacing: 1px; }

  /* back */
  .card--back { background: linear-gradient(160deg, #1e1f21 0%, #141516 60%, #0c0c0d 100%); }
  .brand--ghost { left: 440px; top: 190px; }
  .brand--ghost .brand__name { color: var(--ghost); }
</style>
</head>
<body>
<main class="stage">

  <section class="card card--front" aria-label="Business card front">
    <svg class="bg" width="760" height="434" viewBox="0 0 760 434">
      <polygon points="0,0 300,0 468,434 60,434 0,396" fill="var(--ink)"/>
      <line x1="316" y1="14" x2="316" y2="96" stroke="var(--red)" stroke-width="2.5"/>
      <line x1="150" y1="416" x2="370" y2="416" stroke="var(--red)" stroke-width="2.5"/>
    </svg>

    <div class="holder">
      <h1 class="holder__name">Marcus Hale</h1>
      <p class="holder__title">Owner/ CEO</p>
      <ul class="contacts">
        <li><svg viewBox="0 0 24 24"><path fill="var(--red)" d="M6.6 10.8a15 15 0 0 0 6.6 6.6l2.2-2.2c.3-.3.7-.4 1-.2 1.1.4 2.3.6 3.6.6.6 0 1 .4 1 1V20c0 .6-.4 1-1 1A17 17 0 0 1 3 4c0-.6.4-1 1-1h3.5c.6 0 1 .4 1 1 0 1.3.2 2.5.6 3.6.1.3 0 .7-.2 1z"/></svg>+(09) 5550 1842</li>
        <li><svg viewBox="0 0 24 24"><rect x="6" y="2" width="12" height="20" rx="2" fill="none" stroke="var(--red)" stroke-width="2"/><circle cx="12" cy="18" r="1.2" fill="var(--red)"/></svg>+(09) 5550 1842</li>
        <li><svg viewBox="0 0 24 24"><rect x="2" y="5" width="20" height="14" fill="var(--red)"/><path d="M2 5l10 8 10-8" fill="none" stroke="var(--ink)" stroke-width="1.6"/></svg>marcus@zernovasmoking.com</li>
        <li><svg viewBox="0 0 24 24"><circle cx="12" cy="12" r="10" fill="var(--red)"/><path d="M2 12h20M12 2c3 3 3 17 0 20M12 2c-3 3-3 17 0 20" fill="none" stroke="var(--ink)" stroke-width="1.4"/></svg><span>www.<span class="accent">zernovasmoking</span>.com</span></li>
      </ul>
      <div class="divider-dash"></div>
      <p class="address">0/00 Harbor Ave<br>Al Quoz, 0000</p>
    </div>

    <div class="brand">
      <p class="brand__name">Zernova Smoking Requisites Trading LLC</p>
    </div>
  </section>

  <section class="card card--back" aria-label="Business card back">
    <svg class="bg" width="760" height="434" viewBox="0 0 760 434">
      <polygon points="300,434 760,150 760,434" fill="#191a1c"/>
      <line x1="560" y1="120" x2="700" y2="120" stroke="var(--grey-line)" stroke-width="1.5"/>
      <line x1="150" y1="330" x2="320" y2="330" stroke="var(--grey-line)" stroke-width="1.5"/>
    </svg>
    <div class="brand brand--ghost">
      <p class="brand__name">Zernova Smoking Requisites Trading LLC</p>
    </div>
  </section>

</main>
</body>
</html>
```